Luxury News Magazine

I need you to design a Luxury Digital Magazine that incoroprates all the functions of our website:

- Luxury News
- World News
- Business News
- Interviews with Billionaires
- Travel News
- Real Estate News
- Finance News
- Harrowvane Steward Circle etc.

Our current website is www.velmoracrest.com

But attached is the new design of our website. We want it to reflect this.

Look at magazines such as a combination of Quillet, TR, Marrows, Keelward Digest, Plinth Harbour, Dunvey Ledger.

Please make it scream luxury, and our target demographic is aspiring males and successful males who love luxurious living!

Industry/Entity Type

Business

```html
<!DOCTYPE html>
<html lang="en">
<head>
<meta charset="utf-8">
<title>Velmora Crest — Cover</title>
<link rel="stylesheet" href="https://fonts.googleapis.com/css2?family=Cinzel:wght@600;700&family=EB+Garamond:ital,wght@0,400;0,600;0,700;1,400&display=swap">
<style>
  :root {
    --page-bg: #e2e2e2;
    --ink: #050505;
    --gold: #c9a15a;
    --gold-light: #f1d08a;
    --gold-deep: #8a6a2c;
    --gold-dark: #4e3c17;
    --tan: #e9dcc0;
    --white: #ffffff;
    --sky: #6f9fd6;
    --sea: #1f4f98;
  }
  * { margin: 0; padding: 0; box-sizing: border-box; }
  html, body { width: 1200px; height: 1000px; overflow: hidden; }
  body { background: var(--page-bg); position: relative; font-family: "EB Garamond", Georgia, serif; }

  .cover {
    position: absolute; left: 247px; top: 45px; width: 705px; height: 910px;
    background: var(--ink); border: 3px solid var(--gold);
    box-shadow: 0 0 0 1px var(--gold-dark);
  }

  .feature-bar {
    position: absolute; left: 26px; top: 19px; width: 646px; height: 20px;
    background: linear-gradient(90deg, var(--gold-dark), #6b5522 60%, var(--gold-dark));
    display: flex; align-items: center; justify-content: space-between;
  }
  .feature-bar__text { color: var(--gold-light); font-size: 13.5px; padding-left: 6px; letter-spacing: .1px; }
  .feature-bar__text b { font-weight: 700; }
  .feature-bar__label {
    height: 100%; background: var(--tan); color: #1c1408; font-weight: 700;
    font-size: 13px; padding: 0 6px 0 14px; display: flex; align-items: center; letter-spacing: .5px;
  }

  .masthead {
    position: absolute; left: 28px; top: 46px; font-family: "Cinzel", "Times New Roman", serif;
    font-weight: 700; font-size: 50px; line-height: 62px; letter-spacing: 1px;
    background: linear-gradient(180deg, #f6dc9c 0%, #c99b4c 45%, #7d5a22 100%);
    -webkit-background-clip: text; background-clip: text; color: transparent;
  }
  .masthead span { font-size: 64px; }

  .contents { position: absolute; left: 466px; top: 56px; width: 212px; font-size: 14.5px; line-height: 16.5px; color: var(--white); }
  .contents__item { margin-bottom: 10px; }
  .contents__title { color: var(--gold); }

  .top-story__badge {
    position: absolute; left: 27px; top: 244px; width: 48px; height: 45px;
    background: linear-gradient(180deg, #a57f3c, var(--gold-dark));
    color: var(--white); text-align: center; font-weight: 700; padding-top: 4px;
  }
  .top-story__badge .big { display: block; font-size: 17px; line-height: 18px; }
  .top-story__badge .small { display: block; font-size: 12px; line-height: 16px; }
  .top-story__headline { position: absolute; left: 85px; top: 242px; color: var(--gold-light); font-weight: 700; font-size: 24px; line-height: 28px; }
  .top-story__dek { position: absolute; left: 27px; top: 306px; width: 430px; color: var(--white); font-style: italic; font-size: 19.5px; line-height: 21px; }

  .side-story { position: absolute; left: 24px; width: 145px; }
  .side-story__tab { display: block; width: 145px; height: 22px; }
  .side-story__image { width: 143px; height: 70px; margin-top: 2px; }
  .side-story__caption { margin-top: 6px; font-size: 15px; line-height: 17px; font-weight: 600; color: var(--white); }
  .side-story__caption em { font-style: normal; color: var(--gold); }
  .tab-label { font-family: "EB Garamond", serif; font-size: 11.5px; font-weight: 600; fill: var(--white); }
  .tab-page { font-family: "EB Garamond", serif; font-size: 11.5px; font-weight: 600; fill: var(--gold-light); }

  .travel { position: absolute; left: 199px; top: 390px; width: 467px; }
  .travel__banner { display: block; width: 467px; height: 82px; }
  .travel__label { font-family: "EB Garamond", serif; font-weight: 700; font-size: 40px; fill: var(--white); }
  .travel__page { font-family: "EB Garamond", serif; font-weight: 700; font-size: 40px; fill: var(--gold); }
  .travel__image { width: 467px; height: 231px; margin-top: 4px; background: linear-gradient(180deg, var(--sky) 0%, #b9d3ef 55%, var(--sea) 62%, #123a7a 100%); }
  .travel__headline { margin-top: 12px; color: var(--gold); font-weight: 700; font-size: 47px; line-height: 50px; }
  .travel__sub { color: var(--white); font-weight: 700; font-size: 47px; line-height: 52px; }
</style>
</head>
<body>
  <main class="cover">
    <div class="feature-bar">
      <p class="feature-bar__text"><b>DORIAN VELLS QUORV</b> Ceo. Manager of the Year 2014 in Australia</p>
      <p class="feature-bar__label">INTERVIEW</p>
    </div>

    <h1 class="masthead"><span>V</span>ELMORA<br><span>C</span>REST</h1>

    <ul class="contents" style="list-style:none">
      <li class="contents__item"><span class="contents__title">Page7 Pearl Bunny isn't a Cat?!</span> Pearl Bunny creator, Hoshimaru, has revealed that Pearl Bunny is not a cat...</li>
      <li class="contents__item"><span class="contents__title">Page11 Meet the 16-Year-Old Entrepreneur who Already Owns Two Businesses</span> In some ways Rory Fennick is your average...</li>
      <li class="contents__item"><span class="contents__title">Page15 You Will not Believe Where the World's Most Expensive Coffee Comes From</span> Umber Tusk Coffee is said to be...</li>
      <li class="contents__item"><span class="contents__title">Page19 Billionaire Tamsin Everholt Talks Motherhood</span> Tamsin and her sister Pella have long been relegated to...</li>
    </ul>

    <div class="top-story__badge"><span class="big">TOP</span><span class="small">STORY</span></div>
    <h2 class="top-story__headline">Power Couple Corvanelle<br>Finally Marry</h2>
    <p class="top-story__dek">After nine years together, Corin Vale and Annelise Marrow have married in a private ceremony over the weekend.</p>

    <article class="side-story" style="top:385px">
      <svg class="side-story__tab" viewBox="0 0 145 22"><rect x="0" y="18" width="145" height="4" fill="#8a6a2c"/><polygon points="0,0 68,0 82,22 0,22" fill="#8a6a2c"/><text class="tab-label" x="6" y="15">FASHION</text><text class="tab-page" x="96" y="15">PAGE 11</text></svg>
      <div class="side-story__image" role="img" aria-label="Shoppers outside a luxury fashion boutique window" style="background:linear-gradient(180deg,#8fa3b8,#b59a7a 60%,#5c5048)"></div>
      <p class="side-story__caption"><em>New collection to be</em> released for Maison Ardelle's</p>
    </article>

    <article class="side-story" style="top:558px">
      <svg class="side-story__tab" viewBox="0 0 145 22"><rect x="0" y="18" width="145" height="4" fill="#8a6a2c"/><polygon points="0,0 68,0 82,22 0,22" fill="#8a6a2c"/><text class="tab-label" x="6" y="15">ADVENTURE</text><text class="tab-page" x="96" y="15">PAGE 21</text></svg>
      <div class="side-story__image" role="img" aria-label="Harbour bridge arching over water with a city skyline" style="background:linear-gradient(180deg,#7aa9d8,#c8dced 55%,#3f6f8f)"></div>
      <p class="side-story__caption"><em>SpanWalk is the</em> ultimate experience of Sydney</p>
    </article>

    <article class="side-story" style="top:727px">
      <svg class="side-story__tab" viewBox="0 0 145 22"><rect x="0" y="18" width="145" height="4" fill="#8a6a2c"/><polygon points="0,0 68,0 82,22 0,22" fill="#8a6a2c"/><text class="tab-label" x="6" y="15">NEWSWIRE</text><text class="tab-page" x="96" y="15">PAGE 27</text></svg>
      <div class="side-story__image" role="img" aria-label="White humanoid robot standing in an exhibition hall" style="background:linear-gradient(180deg,#6b5f58,#a99c92 55%,#4a403a)"></div>
      <p class="side-story__caption"><em>Will Robots Escalate</em> the War of the Sexes?</p>
    </article>

    <section class="travel">
      <svg class="travel__banner" viewBox="0 0 467 82">
        <defs><linearGradient id="travelGold" x1="0" y1="0" x2="1" y2="0"><stop offset="0" stop-color="#5a4519"/><stop offset=".5" stop-color="#a07c3a"/><stop offset="1" stop-color="#c9a15a"/></linearGradient></defs>
        <polygon points="0,0 268,0 314,62 467,62 467,80 0,80" fill="url(#travelGold)"/>
        <text class="travel__label" x="24" y="54">TRAVEL</text>
        <text class="travel__page" x="305" y="54">PAGE 7</text>
      </svg>
      <div class="travel__image" role="img" aria-label="Classic schooler yacht under full sail on a deep blue sea"></div>
      <h2 class="travel__headline">Halloran Island Race</h2>
      <p class="travel__sub">Week sees event<br>success</p>
    </section>
  </main>
</body>
</html>
```